VelaMira
Professional
Marnie Tolbeck
Owner
Available for Philadelphia, New Jersey , and New York
VelaMiraPhotography@postvale.com
Im looking for an elagant design... Vela Mira means Bright Sail in italian. My co. is after my baby girl (Lila June)
I photograph Newborns, Babies, maternity, Children, Family's, Engagements, Pets
Baby Face Big smile
Baby Blue/color edit
Mom with Child
bridge city shot
b&w pic of child with fence
flowers with ring

```html
<!DOCTYPE html>
<html lang="en">
<head>
<meta charset="utf-8">
<title>VelaMira Photography – Business Card</title>
<link href="https://fonts.googleapis.com/css2?family=Arimo:wght@400;700&display=swap" rel="stylesheet">
<style>
  :root {
    --page-bg: #d6d6d6;
    --card-top: #2a2a2a;
    --card-bottom: #0b0b0b;
    --text-main: #ffffff;
    --text-soft: #d9d9d9;
    --text-muted: #a8a8a8;
    --accent-blue: #2aa7e8;
    --accent-blue-light: #7fd0f7;
    --photo-border: #f2f2f2;
  }
  html, body {
    margin: 0;
    padding: 0;
    width: 1200px;
    height: 862px;
    overflow: hidden;
    background: var(--page-bg);
    font-family: "Arimo", Arial, sans-serif;
  }
  .canvas {
    position: relative;
    width: 1200px;
    height: 862px;
    display: flex;
    align-items: center;
    justify-content: center;
  }
  .business-card {
    position: relative;
    width: 720px;
    height: 390px;
    border-radius: 26px;
    background: linear-gradient(180deg, var(--card-top) 0%, var(--card-bottom) 100%);
    color: var(--text-main);
    text-align: center;
    overflow: hidden;
  }
  .brand {
    position: absolute;
    top: 34px;
    left: 0;
    right: 0;
  }
  .brand-name {
    margin: 0;
    font-size: 58px;
    font-weight: 400;
    letter-spacing: 1px;
    color: var(--text-main);
    line-height: 1;
  }
  .brand-tagline {
    margin: 14px 0 0;
    font-size: 17px;
    letter-spacing: 4px;
    color: var(--text-muted);
  }
  .side-tab {
    position: absolute;
    top: 168px;
    width: 22px;
    height: 62px;
    background: linear-gradient(90deg, var(--accent-blue) 0%, var(--accent-blue-light) 50%, var(--accent-blue) 100%);
  }
  .side-tab--left { left: 0; }
  .side-tab--right { right: 0; }
  .photo-strip {
    position: absolute;
    top: 140px;
    left: 0;
    right: 0;
    display: flex;
    justify-content: center;
    gap: 14px;
  }
  .photo-frame {
    width: 190px;
    height: 122px;
    border: 3px solid var(--photo-border);
    box-sizing: border-box;
  }
  .photo-frame--smile {
    transform: rotate(-3deg);
    background: linear-gradient(135deg, #e9c3a6 0%, #c98e70 55%, #8a5a45 100%);
  }
  .photo-frame--mono {
    transform: rotate(1deg);
    background: linear-gradient(135deg, #e6e6e6 0%, #9a9a9a 55%, #4a4a4a 100%);
  }
  .photo-frame--flowers {
    transform: rotate(3deg);
    background: linear-gradient(135deg, #c7a17f 0%, #e3b7c8 55%, #b97ca5 100%);
  }
  .contact {
    position: absolute;
    top: 284px;
    left: 0;
    right: 0;
  }
  .contact-name {
    margin: 0 0 6px;
    font-size: 20px;
    font-weight: 700;
  }
  .contact-line {
    margin: 0;
    font-size: 17px;
    line-height: 22px;
    color: var(--text-soft);
  }
  .contact-divider { padding: 0 8px; }
</style>
</head>
<body>
  <main class="canvas">
    <article class="business-card">
      <header class="brand">
        <h1 class="brand-name">VelaMira</h1>
        <p class="brand-tagline">Photography</p>
      </header>

      <span class="side-tab side-tab--left"></span>
      <span class="side-tab side-tab--right"></span>

      <section class="photo-strip">
        <div class="photo-frame photo-frame--smile" role="img" aria-label="Baby with a big smile"></div>
        <div class="photo-frame photo-frame--mono" role="img" aria-label="Black and white portrait of a young child"></div>
        <div class="photo-frame photo-frame--flowers" role="img" aria-label="Baby sitting among pink flowers"></div>
      </section>

      <section class="contact">
        <p class="contact-name">Marnie Tolbeck</p>
        <p class="contact-line">Philadelphia, New Jersey, and New York.</p>
        <p class="contact-line">Phone: 555-014-2290. Cell: 555-017-3846.</p>
        <p class="contact-line">Email: Marnie@VelaMira.net<span class="contact-divider">|</span>www.velamira.net</p>
      </section>
    </article>
  </main>
</body>
</html>
```